Business card design for a Cloud Service Provider Company

We already have business card and would like to update and get a different design. Our company is Managed IT services and Cloud Solutions Company, Tevro Systems. Attached is our current logo, current business card and sample design. I am not sure if we still need to keep our partners details on the back of the card as it does not look good to me... Please let me know if you need any additional information...

Target Market(s)

Any verticals with IT infrastructure - CEOs, CFOs and CIOs

Industry/Entity Type

Information Technology

Requirements
Must have
• First Name Last Name
• Phone
• Email address
• Company Logo

```html
<!DOCTYPE html>
<html lang="en">
<head>
<meta charset="utf-8">
<title>Tevro Systems – Business Card</title>
<link rel="stylesheet" href="https://fonts.googleapis.com/css2?family=Open+Sans:wght@400;600;700&display=swap">
<style>
  :root {
    --bg: #3a3431;
    --card: #050505;
    --card-sheen: #1a1a1a;
    --green: #8fd11a;
    --blue: #1fb3e0;
    --white: #f2f2f2;
    --grey: #cfcfcf;
    --font: "Open Sans", Arial, sans-serif;
  }
  * { margin: 0; padding: 0; box-sizing: border-box; }
  html, body { width: 1200px; height: 844px; overflow: hidden; }
  body {
    background: var(--bg);
    font-family: var(--font);
    position: relative;
  }
  .card {
    position: absolute;
    top: 263px;
    width: 520px;
    height: 318px;
    background: radial-gradient(ellipse at 55% 35%, var(--card-sheen), var(--card) 70%);
    box-shadow: 0 10px 30px rgba(0,0,0,.45);
    overflow: hidden;
  }
  .card--front { left: 50px; }
  .card--back { left: 630px; }

  /* Front */
  .band { position: absolute; left: 0; right: 0; height: 14px; }
  .band--top { top: 0; background: linear-gradient(#a6e22a, var(--green)); }
  .band--bottom { bottom: 0; background: linear-gradient(#3cc6ef, var(--blue)); }
  .contact-block {
    position: absolute;
    left: 200px;
    top: 108px;
  }
  .person-name {
    color: var(--green);
    font-weight: 700;
    font-size: 19px;
    letter-spacing: .2px;
  }
  .person-title {
    color: var(--white);
    font-size: 13.5px;
    margin: 2px 0 0 16px;
  }
  .contact-list { list-style: none; margin-top: 24px; }
  .contact-item {
    display: flex;
    align-items: center;
    gap: 10px;
    color: var(--white);
    font-size: 15px;
    margin-bottom: 6px;
    margin-left: 24px;
  }
  .contact-item--email { margin-left: 0; }
  .contact-icon { width: 14px; height: 14px; flex: none; }

  /* Back */
  .address {
    position: absolute;
    top: 44px; left: 0; right: 0;
    text-align: center;
    color: var(--white);
    font-size: 12.5px;
  }
  .brand {
    position: absolute;
    top: 92px; left: 0; right: 0;
    text-align: center;
    color: var(--grey);
    font-weight: 700;
    font-size: 66px;
    letter-spacing: -1px;
    line-height: 1;
  }
  .website {
    position: absolute;
    top: 190px; left: 0; right: 0;
    text-align: center;
    color: var(--white);
    font-size: 14px;
  }
  .support {
    position: absolute;
    top: 218px; left: 0; right: 0;
    text-align: center;
    color: var(--white);
    font-size: 15px;
  }
  .support-label { color: var(--green); font-weight: 700; }
  .tab { position: absolute; width: 22px; height: 40px; }
  .tab--green { left: 0; top: 200px; background: linear-gradient(90deg, #7fc014, var(--green)); }
  .tab--blue { right: 0; top: 14px; background: linear-gradient(90deg, #189ccb, var(--blue)); }
</style>
</head>
<body>
  <section class="card card--front" aria-label="Business card front">
    <div class="band band--top"></div>
    <div class="contact-block">
      <h1 class="person-name">Dane R.Colvar</h1>
      <p class="person-title">Technical Manager</p>
      <ul class="contact-list">
        <li class="contact-item">
          <svg class="contact-icon" viewBox="0 0 14 14" aria-hidden="true"><path d="M3 1 L5 4 L4 5.5 C5 7.5 6.5 9 8.5 10 L10 9 L13 11 L11.5 13 C6 12.5 1.5 8 1 2.5 Z" fill="var(--green)"/></svg>
          61 25550 1842
        </li>
        <li class="contact-item">
          <svg class="contact-icon" viewBox="0 0 14 14" aria-hidden="true"><rect x="3" y="1" width="8" height="12" rx="1.5" fill="none" stroke="var(--green)" stroke-width="1.6"/></svg>
          61 455 019 276
        </li>
        <li class="contact-item contact-item--email">
          <svg class="contact-icon" viewBox="0 0 14 14" aria-hidden="true"><rect x="1" y="3" width="12" height="8" fill="var(--green)"/><path d="M1 3 L7 8 L13 3" fill="none" stroke="var(--card)" stroke-width="1.2"/></svg>
          dane.colvar@tevro.com.au
        </li>
      </ul>
    </div>
    <div class="band band--bottom"></div>
  </section>

  <section class="card card--back" aria-label="Business card back">
    <div class="tab tab--blue"></div>
    <p class="address">Level 14 88 Harbour Lane Sydney, NSW 2000</p>
    <p class="brand">Tevro</p>
    <p class="website">www.tevro.com.au</p>
    <p class="support"><span class="support-label">Support:</span> 1300 555 912</p>
    <div class="tab tab--green"></div>
  </section>
</body>
</html>
```